Beacon Advisory Website

I currently have a website www.beaconadvisoryinc.example. We are a IT Consulting Company. Our website will pretty much tell out our services. I am looking to enhance my website and make it look more professional. Looking for very classy and Contemporary look and design for my website.

Industry/Entity Type

It Company

```html
<!DOCTYPE html>
<html lang="en">
<head>
<meta charset="utf-8">
<title>Beacon Advisory</title>
<link rel="stylesheet" href="https://fonts.googleapis.com/css2?family=Fira+Sans:wght@300;400;500;600;700&family=Open+Sans:wght@400;600;700&family=Arimo:ital,wght@0,400;0,700;1,400;1,700&display=swap">
<style>
:root{
  --brand-blue:#1a64b4;
  --sky:#019fdb;
  --ink:#2f2f2f;
  --text:#4a4a4a;
  --dark:#303133;
  --footer:#0d4592;
  --white:#ffffff;
  --line:#d6d6d6;
}
*{margin:0;padding:0;box-sizing:border-box}
html,body{width:1200px;height:2452px;overflow:hidden}
body{position:relative;background:var(--white);font-family:"Open Sans",sans-serif;color:var(--text)}
.abs{position:absolute}

/* header */
.site-header{position:absolute;left:0;top:0;width:1200px;height:108px;background:var(--white);border-bottom:1px solid #e8e8e8}
.brand{position:absolute;left:72px;top:30px;display:flex;align-items:center;gap:12px}
.brand-dot{width:40px;height:40px;border-radius:50%;background:var(--brand-blue)}
.brand-name{font-family:"Fira Sans",sans-serif;font-weight:700;font-size:26px;color:var(--brand-blue);letter-spacing:.5px}
.social-top{position:absolute;left:905px;top:10px;display:flex;gap:3px}
.diamond{width:30px;height:30px;display:block}
.lang{position:absolute;left:1052px;top:16px;font-size:13px;color:#333;display:flex;align-items:center;gap:7px}
.lang-flag{width:16px;height:10px;background:#c8102e;border:2px solid #1f3b86}
.caret{width:0;height:0;border-left:4px solid transparent;border-right:4px solid transparent;border-top:5px solid #333}
.main-nav{position:absolute;top:70px;left:0;width:1200px;height:38px}
.main-nav a{position:absolute;font-size:15px;color:#333;text-decoration:none;transform:translateX(-50%);white-space:nowrap}
.main-nav .active::after{content:"";position:absolute;left:-10px;right:-10px;top:30px;height:4px;background:var(--sky)}

/* hero */
.hero{position:absolute;left:0;top:108px;width:1200px;height:459px;background:linear-gradient(90deg,#e3e4e6 0%,#eef0f1 45%,#e9eaec 100%)}
.hero-photo{position:absolute;left:115px;top:0;width:380px;height:459px;background:linear-gradient(180deg,#d9d4cf 0%,#ece9e6 45%,#f3f3f3 100%)}
.hero-kicker{position:absolute;left:548px;top:88px;font-family:"Fira Sans",sans-serif;font-weight:300;font-size:46px;color:#333;letter-spacing:1px}
.hero-title{position:absolute;left:546px;top:140px;font-family:"Fira Sans",sans-serif;font-weight:700;font-size:72px;color:var(--brand-blue);letter-spacing:1px}
.hero-copy{position:absolute;left:549px;top:230px;width:555px;font-size:14.5px;line-height:23px;color:#444}
.btn-outline{position:absolute;left:549px;top:325px;width:141px;height:51px;border:2px solid var(--brand-blue);font-size:16px;color:#333;display:flex;align-items:center;justify-content:center;letter-spacing:.5px}

/* about */
.about{position:absolute;left:0;top:567px;width:1200px;height:169px;background:var(--sky);color:var(--white)}
.about-title{position:absolute;left:88px;top:30px;font-family:"Fira Sans",sans-serif;font-weight:700;font-size:52px;line-height:60px}
.about-sub{position:absolute;left:88px;top:90px;font-family:"Fira Sans",sans-serif;font-size:28px}
.about-rule{position:absolute;left:360px;top:22px;width:1px;height:117px;background:rgba(255,255,255,.8)}
.about-copy{position:absolute;left:384px;top:24px;width:745px;font-size:14.5px;line-height:20px}

/* features */
.feature{position:absolute;top:818px;width:330px;text-align:center;transform:translateX(-50%)}
.feature-icon{width:102px;height:102px;margin:0 auto;display:block}
.feature-title{font-family:"Fira Sans",sans-serif;font-weight:500;font-size:31px;color:var(--ink);margin-top:24px;line-height:40px}
.feature-copy{font-size:13.5px;line-height:22px;color:#444;margin-top:14px}
.feature-link{display:block;margin-top:17px;font-family:"Fira Sans",sans-serif;font-weight:600;font-size:14px;color:var(--brand-blue);letter-spacing:.5px}

/* services band */
.services{position:absolute;left:0;top:1246px;width:1200px;height:423px;background:radial-gradient(ellipse at 50% 40%,#4a4b4d 0%,#363739 50%,#2b2c2e 100%)}
.service{position:absolute;width:300px}
.service-icon{position:absolute;left:0;top:4px;width:50px;height:50px}
.service-title{position:absolute;left:64px;top:0;font-family:"Fira Sans",sans-serif;font-weight:600;font-size:18px;color:var(--white);white-space:nowrap}
.service-copy{position:absolute;left:64px;top:28px;width:230px;font-size:13.5px;line-height:20px;color:#f0f0f0}

/* testimonial */
.section-heading{position:absolute;left:0;top:1722px;width:1200px;text-align:center;font-family:"Fira Sans",sans-serif;font-size:29px;color:#222;letter-spacing:.5px}
.quote{position:absolute;left:90px;top:1806px;width:1020px;text-align:center;font-family:"Arimo",sans-serif;font-style:italic;font-size:17.5px;line-height:25px;color:#444}
.avatar{position:absolute;left:543px;top:1884px;width:114px;height:114px;border-radius:50%;background:linear-gradient(160deg,#d9d9d9,#a8a8a8);border:4px solid #e6e6e6}
.quote-badge{position:absolute;left:533px;top:1882px;width:42px;height:42px;border-radius:50%;background:#333;border:3px solid var(--white)}
.author{position:absolute;left:0;top:2030px;width:1200px;text-align:center;font-family:"Arimo",sans-serif;font-style:italic;font-size:17.5px;color:#333}
.author b{font-weight:700;letter-spacing:.5px}
.pager{position:absolute;left:546px;top:2092px;display:flex;gap:6px}
.pager span{width:31px;height:6px;background:#d4d4d4}
.pager .on{background:var(--sky)}

/* footer */
.site-footer{position:absolute;left:0;top:2147px;width:1200px;height:305px;background:var(--footer);color:var(--white);text-align:center}
.footer-brand{position:absolute;left:0;top:52px;width:1200px;display:flex;justify-content:center;align-items:center;gap:12px}
.footer-brand .brand-dot{background:var(--white)}
.footer-brand .brand-name{color:var(--white)}
.footer-links{position:absolute;left:0;top:128px;width:1200px;font-family:"Fira Sans",sans-serif;font-size:17px;letter-spacing:.3px}
.copyright{position:absolute;left:0;top:156px;width:1200px;font-family:"Fira Sans",sans-serif;font-size:16.5px}
.social-foot{position:absolute;left:510px;top:214px;display:flex;gap:4px}
.social-foot .diamond{width:40px;height:40px}
</style>
</head>
<body>

<header class="site-header">
  <div class="brand"><span class="brand-dot"></span><span class="brand-name">BEACON ADVISORY</span></div>
  <div class="social-top">
    <svg class="diamond" viewBox="0 0 30 30"><rect x="6" y="6" width="18" height="18" transform="rotate(45 15 15)" fill="#222"/></svg>
    <svg class="diamond" viewBox="0 0 30 30"><rect x="6" y="6" width="18" height="18" transform="rotate(45 15 15)" fill="#222"/></svg>
    <svg class="diamond" viewBox="0 0 30 30"><rect x="6" y="6" width="18" height="18" transform="rotate(45 15 15)" fill="#222"/></svg>
    <svg class="diamond" viewBox="0 0 30 30"><rect x="6" y="6" width="18" height="18" transform="rotate(45 15 15)" fill="#222"/></svg>
  </div>
  <div class="lang"><span class="lang-flag"></span>English<span class="caret"></span></div>
  <nav class="main-nav">
    <a class="active" style="left:642px">Home page</a>
    <a style="left:767px">Solutions</a>
    <a style="left:880px">Services</a>
    <a style="left:994px">Company</a>
    <a style="left:1107px">Contact</a>
  </nav>
</header>

<section class="hero">
  <div class="hero-photo" role="img" aria-label="Photo of a smiling consultant in glasses and a white sweater, arms folded, in a bright office"></div>
  <div class="hero-kicker">SOLUTIONS,</div>
  <div class="hero-title">THAT YOU NEED!</div>
  <p class="hero-copy">Your company works hard to generate new business and stay competitive, so understanding how your products fare in the market, understanding customer buying habits, or even understanding where your sales force is failing, can give you the edge you need.</p>
  <div class="btn-outline">READ MORE</div>
</section>

<section class="about">
  <div class="about-title">About</div>
  <div class="about-sub">Beacon Advisory</div>
  <div class="about-rule"></div>
  <p class="about-copy">Today's IT market is a dynamic, fast-paced industry, with ever-increasing demands. Meeting these demands for over 25 years, Beacon Advisory maintains a global presence, aggressively recruiting expertly qualified IT and Management Professionals from around the world and cultivating key partnerships with corporations to understand their business models end-to-end, with a goal of delivering exceptional client service and ensuring a consistent delivery of the talent needed to drive results.</p>
</section>

<div class="feature" style="left:234px">
  <svg class="feature-icon" viewBox="0 0 100 100">
    <path d="M47 50 L47 2 A48 48 0 0 0 2 47 Z" fill="#555"/>
    <path d="M47 53 L2 53 A48 48 0 0 0 47 98 Z" fill="#555"/>
    <path d="M53 2 A48 48 0 0 1 98 47 L53 47 Z" fill="none" stroke="#1a64b4" stroke-width="4"/>
    <path d="M53 53 L98 53 A48 48 0 0 1 53 98 Z" fill="#1a64b4"/>
  </svg>
  <div class="feature-title">Dashbords</div>
  <p class="feature-copy">Viewing key business metrics in an intuitive format enables empowered management to quickly make critical operating decisions; intelligent sales force deployment, re-alignment of marketing initiatives, risk concentration analysis for the insurance industry, or human capital optimization.</p>
  <span class="feature-link">READ MORE</span>
</div>

<div class="feature" style="left:600px">
  <svg class="feature-icon" viewBox="0 0 100 100">
    <circle cx="50" cy="50" r="50" fill="#1a64b4"/>
    <circle cx="44" cy="44" r="14" fill="#fff"/>
    <path d="M20 82 Q44 54 68 82 Z" fill="#fff"/>
    <path d="M58 40 L66 48 L82 28" fill="none" stroke="#fff" stroke-width="6"/>
  </svg>
  <div class="feature-title">Data Warehousing</div>
  <p class="feature-copy">Viewing key business metrics in an intuitive format enables empowered management to quickly make critical operating decisions; intelligent sales force deployment, re-alignment of marketing initiatives, risk concentration analysis for the insurance industry, or human capital optimization.</p>
  <span class="feature-link">READ MORE</span>
</div>

<div class="feature" style="left:971px">
  <svg class="feature-icon" viewBox="0 0 100 100">
    <circle cx="50" cy="50" r="50" fill="#1a64b4"/>
    <rect x="44" y="26" width="34" height="28" fill="none" stroke="#fff" stroke-width="4"/>
    <circle cx="34" cy="36" r="7" fill="#fff"/>
    <rect x="28" y="46" width="13" height="30" fill="#fff"/>
    <path d="M58 54 L52 72 M64 54 L70 72" stroke="#fff" stroke-width="3"/>
  </svg>
  <div class="feature-title">BPM</div>
  <p class="feature-copy">Viewing key business metrics in an intuitive format enables empowered management to quickly make critical operating decisions; intelligent sales force deployment, re-alignment of marketing initiatives, risk concentration analysis for the insurance industry, or human capital optimization.</p>
  <span class="feature-link">READ MORE</span>
</div>

<section class="services" role="img" aria-label="Dark blurred photo of a desk with a laptop and monitor behind the services list">
  <div class="service" style="left:85px;top:70px">
    <svg class="service-icon" viewBox="0 0 50 50"><circle cx="25" cy="25" r="22" fill="none" stroke="#019fdb" stroke-width="3"/><ellipse cx="25" cy="25" rx="9" ry="20" fill="none" stroke="#019fdb" stroke-width="2"/><path d="M5 25 H45" stroke="#019fdb" stroke-width="2"/></svg>
    <div class="service-title">Technology</div>
    <p class="service-copy">Company that offers design and build services for you from initial sketches to the final production.</p>
  </div>
  <div class="service" style="left:469px;top:70px">
    <svg class="service-icon" viewBox="0 0 50 50"><circle cx="25" cy="25" r="22" fill="none" stroke="#019fdb" stroke-width="3" stroke-dasharray="30 6"/><circle cx="25" cy="25" r="12" fill="#019fdb"/></svg>
    <div class="service-title">Business</div>
    <p class="service-copy">Company that offers design and build services for you from initial sketches to the final production.</p>
  </div>
  <div class="service" style="left:820px;top:70px">
    <svg class="service-icon" viewBox="0 0 50 50"><circle cx="25" cy="25" r="22" fill="none" stroke="#019fdb" stroke-width="2"/><rect x="16" y="14" width="18" height="22" fill="none" stroke="#019fdb" stroke-width="3"/></svg>
    <div class="service-title">Application Developement</div>
    <p class="service-copy">Company that offers design and build services for you from initial sketches to the final production.</p>
  </div>
  <div class="service" style="left:85px;top:254px">
    <svg class="service-icon" viewBox="0 0 50 50"><circle cx="25" cy="25" r="24" fill="#019fdb"/><rect x="14" y="22" width="22" height="12" fill="#1b3f6b"/><rect x="19" y="14" width="12" height="8" fill="#1b3f6b"/></svg>
    <div class="service-title">Enterprise Integration</div>
    <p class="service-copy">Company that offers design and build services for you from initial sketches to the final production.</p>
  </div>
  <div class="service" style="left:469px;top:254px">
    <svg class="service-icon" viewBox="0 0 50 50"><circle cx="25" cy="25" r="24" fill="#019fdb"/><circle cx="25" cy="25" r="14" fill="none" stroke="#fff" stroke-width="3"/><rect x="19" y="22" width="12" height="9" fill="#fff"/></svg>
    <div class="service-title">IT Consulting</div>
    <p class="service-copy">Company that offers design and build services for you from initial sketches to the final production.</p>
  </div>
  <div class="service" style="left:820px;top:254px">
    <svg class="service-icon" viewBox="0 0 50 50"><circle cx="25" cy="25" r="24" fill="#019fdb"/><rect x="12" y="14" width="26" height="18" fill="none" stroke="#1b3f6b" stroke-width="3"/><rect x="18" y="34" width="14" height="3" fill="#1b3f6b"/></svg>
    <div class="service-title">Staff Augmentation</div>
    <p class="service-copy">Company that offers design and build services for you from initial sketches to the final production.</p>
  </div>
</section>

<h2 class="section-heading">WHAT PEOPLE SAY</h2>
<p class="quote">"Lorem ipsum dolor sit amet, consectetur adipiscing elit. Morbi hendrerit elit turpis, a porttitor tellus sollicitudin at. Class aptent taciti sociosqu ad litora torquent per conubia nostra, per inceptos himenaeos."</p>
<div class="avatar" role="img" aria-label="Portrait photo of the client giving the testimonial"></div>
<svg class="quote-badge" viewBox="0 0 42 42"><circle cx="16" cy="22" r="4" fill="#fff"/><circle cx="26" cy="22" r="4" fill="#fff"/><path d="M13 22 Q13 15 18 14 M23 22 Q23 15 28 14" stroke="#fff" stroke-width="2.5" fill="none"/></svg>
<div class="author"><b>MARISSA COLTON</b> Fitness Enthuisast, BROOKFIELD</div>
<div class="pager"><span class="on"></span><span></span><span></span><span></span></div>

<footer class="site-footer">
  <div class="footer-brand"><span class="brand-dot"></span><span class="brand-name">BEACON ADVISORY</span></div>
  <div class="footer-links">HOME • SOLUTIONS • SERVICES • COMPANY • CONTACT</div>
  <div class="copyright">Copyright © 2007 - 2015 Norvale Software, Inc. All Rights Reserved</div>
  <div class="social-foot">
    <svg class="diamond" viewBox="0 0 40 40"><rect x="8" y="8" width="24" height="24" transform="rotate(45 20 20)" fill="#111"/></svg>
    <svg class="diamond" viewBox="0 0 40 40"><rect x="8" y="8" width="24" height="24" transform="rotate(45 20 20)" fill="#111"/></svg>
    <svg class="diamond" viewBox="0 0 40 40"><rect x="8" y="8" width="24" height="24" transform="rotate(45 20 20)" fill="#111"/></svg>
    <svg class="diamond" viewBox="0 0 40 40"><rect x="8" y="8" width="24" height="24" transform="rotate(45 20 20)" fill="#111"/></svg>
  </div>
</footer>

</body>
</html>
```